Golden Harbor Market VIP Card(Magnetic strip plastic card)

We need Fancy,Simple,VIP customer card design for a grocery store name"Golden Harbor Market", Chinese name"金港商场“.Major color should be Dark red. This design is based on a VIP gift card project, which means design should consider about the back side with magnetic strip area and mostly it will be plastic material.

Target Market(s)

Rich Customers

Industry/Entity Type

Grocery Store

Contact Information for Business Card

People actually put more than $1000 into the card for shopping

Font styles to use
Serif
Sans Serif
Decorative
Script
Other font styles liked:
• Fancy

Colors
ec1f27
fbed22

Requirements
Must have
• Red color
Nice to have
• Better logo transformation.

```html
<!DOCTYPE html>
<html lang="en">
<head>
<meta charset="utf-8">
<title>Golden Harbor Market VIP Card</title>
<link rel="stylesheet" href="https://fonts.googleapis.com/css2?family=Arimo&family=Questrial&family=Tinos:wght@700&family=Noto+Sans+SC&display=swap">
<style>
  :root {
    --card-red: #ec1f27;
    --gold: #fbed22;
    --dragon: #f26a2e;
    --fine-print: #f4572b;
    --strip: #000000;
    --page: #ffffff;
  }
  * { box-sizing: border-box; margin: 0; padding: 0; }
  html, body { width: 1200px; height: 1200px; overflow: hidden; background: var(--page); }
  .canvas { position: relative; width: 1200px; height: 1200px; }

  .card {
    position: absolute;
    width: 585px;
    height: 364px;
    background: var(--card-red);
    border-radius: 16px;
    overflow: hidden;
    transform-origin: top left;
  }
  .card--raised { box-shadow: 0 22px 40px rgba(0,0,0,0.28); }
  .card--small { transform: scale(0.802); }

  .front-main { left: 94px; top: 115px; z-index: 2; }
  .back-main { left: 512px; top: 346px; z-index: 1; }
  .front-small { left: 94px; top: 830px; }
  .back-small { left: 627px; top: 830px; }

  .dragon-art { position: absolute; opacity: 0.75; }
  .dragon-art--left {
    left: 0; top: 0; width: 200px; height: 364px;
    background: linear-gradient(90deg, rgba(242,106,46,0.55), rgba(242,106,46,0.15) 80%, rgba(242,106,46,0));
  }
  .dragon-art--crest {
    left: 205px; top: 0; width: 110px; height: 70px;
    border-radius: 0 0 60px 60px;
    background: radial-gradient(ellipse at 50% 0%, rgba(242,106,46,0.45), rgba(242,106,46,0));
  }
  .dragon-art--coil {
    right: 50px; top: 0; width: 170px; height: 90px;
    border-radius: 0 0 90px 90px;
    background: radial-gradient(ellipse at 50% 20%, rgba(242,106,46,0.55), rgba(242,106,46,0));
  }
  .dragon-art--tail {
    right: 0; top: 0; width: 90px; height: 364px;
    background: linear-gradient(270deg, rgba(242,106,46,0.6), rgba(242,106,46,0));
    -webkit-mask-image: linear-gradient(180deg, transparent 0%, #000 30%, #000 100%);
    mask-image: linear-gradient(180deg, transparent 0%, #000 30%, #000 100%);
  }

  .brand {
    position: absolute;
    left: 0; right: 0; top: 44px;
    display: flex; flex-direction: column; align-items: center;
    color: var(--gold);
    font-family: "Arimo", sans-serif;
    font-weight: 400;
    white-space: nowrap;
  }
  .brand__mark {
    width: 26px; height: 26px; border-radius: 50%;
    background: var(--gold);
    margin-bottom: 6px;
  }
  .brand__name-cn {
    font-family: "Noto Sans SC", sans-serif;
    font-size: 40px; line-height: 1.1; letter-spacing: 2px;
  }
  .brand__name-en { font-size: 14px; line-height: 1.3; margin-top: 4px; }

  .tier {
    position: absolute; left: 0; right: 0; top: 190px;
    text-align: center;
    font-family: "Tinos", serif; font-weight: 700;
    font-size: 46px; color: var(--gold);
  }
  .tagline {
    position: absolute; left: 0; right: 0; top: 284px;
    text-align: center;
    font-family: "Arimo", sans-serif;
    font-size: 18.5px; color: var(--gold);
  }

  .holder {
    position: absolute; left: 50px; top: 38px;
    display: flex; align-items: center; gap: 10px;
    font-family: "Questrial", sans-serif;
    font-size: 32px; letter-spacing: 1px; color: var(--gold);
    white-space: nowrap;
  }
  .holder__dot { width: 10px; height: 10px; border-radius: 50%; background: var(--gold); }

  .terms {
    position: absolute; left: 13px; top: 131px; width: 552px;
    font-family: "Arimo", sans-serif;
    font-size: 13.5px; line-height: 16px; letter-spacing: 0.3px;
    color: var(--fine-print);
    text-align: justify;
  }
  .mag-strip {
    position: absolute; left: 0; right: 0; top: 246px; height: 61px;
    background: var(--strip);
  }
</style>
</head>
<body>
<main class="canvas">

  <section class="card card--raised front-main" aria-label="VIP card front">
    <div class="dragon-art dragon-art--left" role="img" aria-label="Orange line-art dragon along the left edge"></div>
    <div class="dragon-art dragon-art--crest" role="img" aria-label="Orange dragon tail curling above the brand name"></div>
    <div class="brand">
      <span class="brand__mark"></span>
      <span class="brand__name-cn">金港商场</span>
      <span class="brand__name-en">Golden Harbor Market</span>
    </div>
    <div class="tier">V.I.P.</div>
    <p class="tagline">People actually put more than $1000 into the card for shopping</p>
  </section>

  <section class="card card--raised back-main" aria-label="VIP card back">
    <div class="dragon-art dragon-art--coil" role="img" aria-label="Orange dragon body coiling at the top right"></div>
    <div class="dragon-art dragon-art--tail" role="img" aria-label="Orange dragon body along the right edge"></div>
    <div class="holder"><span class="holder__dot"></span><span>MARK LEUNG</span></div>
    <p class="terms">This "Card" contains value which may be used to purchase goods with the exception of other Cards. Please present it to a sales associate at the time of purchase and amounts will be deducted from the Card balance. This Card may not be redeemed for cash and the unused value remains on the Card. Merchant is not responsible for lost, stolen or damaged Cards or any unauthorized use.</p>
    <div class="mag-strip"></div>
  </section>

  <section class="card card--small front-small" aria-label="VIP card front, actual size">
    <div class="dragon-art dragon-art--left" role="img" aria-label="Orange line-art dragon along the left edge"></div>
    <div class="dragon-art dragon-art--crest" role="img" aria-label="Orange dragon tail curling above the brand name"></div>
    <div class="brand">
      <span class="brand__mark"></span>
      <span class="brand__name-cn">金港商场</span>
      <span class="brand__name-en">Golden Harbor Market</span>
    </div>
    <div class="tier">V.I.P.</div>
    <p class="tagline">People actually put more than $1000 into the card for shopping</p>
  </section>

  <section class="card card--small back-small" aria-label="VIP card back, actual size">
    <div class="dragon-art dragon-art--coil" role="img" aria-label="Orange dragon body coiling at the top right"></div>
    <div class="dragon-art dragon-art--tail" role="img" aria-label="Orange dragon body along the right edge"></div>
    <div class="holder"><span class="holder__dot"></span><span>MARK LEUNG</span></div>
    <p class="terms">This "Card" contains value which may be used to purchase goods with the exception of other Cards. Please present it to a sales associate at the time of purchase and amounts will be deducted from the Card balance. This Card may not be redeemed for cash and the unused value remains on the Card. Merchant is not responsible for lost, stolen or damaged Cards or any unauthorized use.</p>
    <div class="mag-strip"></div>
  </section>

</main>
</body>
</html>
```